Skill Up Salary Up

Full Page
7.5 w x 10 h / 8 w x 10.75 h + .25" bleed
Full-Page Career Course Ad
Project Overview
• Goal: Create a visually attractive, modern, and uncluttered full-page magazine advertisement to list available career courses.
• Tone: Creative, professional, and attention-grabbing to prevent the reader from turning the page. The final design must prioritize readability.

Content Requirements
1. Header/Headline: Must be the primary focus. And grab peoples attention
2. Course Listing: A clear, well-organized list of the career courses.
________________________________________
Design & Aesthetic Directives
1. Layout & Readability (Crucial)
• The final ad must not look crowded or busy.
• Prioritize white space to make the text "breathe" and ensure the course list is easy to scan and read.
• Use a modern, clean, and professional typeface (font choice is critical for the aesthetic).
2. Visual Style
• Aim for a creative, modern, and fresh look. Avoid outdated or generic stock imagery/layouts.
3. Imagery/Graphic Element (Artist's Choice)
You have creative freedom regarding the main graphic element.
• Option A (Photography): Use a photo of a white male American with a collared shirt. The imagery should convey success, focus, or professional development.
• Option B (Vector/Illustration): Use a modern vector graphic, illustration, or abstract design. This could be used to symbolize growth, connection, or a career path.
The choice of graphic element is yours, but it must support the overall modern and uncrowded aesthetic.

Requirements
Must have
• Partial listing .. is part of the Harbor Lantern Course

```html
<!DOCTYPE html>
<html lang="en">
<head>
<meta charset="utf-8">
<title>Skill Up, Salary Up – Upcoming KTA Courses</title>
<link rel="stylesheet" href="https://fonts.googleapis.com/css2?family=Poppins:wght@400;500;600;700;800&display=swap">
<style>
:root{
  --navy:#14203c;
  --gold:#fba919;
  --gold-soft:#fdc04f;
  --seal-ring:#ffd86b;
  --red:#e0261f;
  --ink:#14203c;
  --paper:#ffffff;
  --band:#c9c9c9;
}
*{box-sizing:border-box;margin:0;padding:0}
html,body{width:940px;height:1200px;overflow:hidden;background:var(--paper)}
body{font-family:'Poppins',sans-serif;color:var(--ink);position:relative}

.hero{position:absolute;left:0;top:0;width:940px;height:215px;background:var(--navy);text-align:center}
.hero__kicker{position:absolute;top:30px;width:100%;font-size:66px;font-weight:500;color:var(--gold);letter-spacing:1px;line-height:1}
.hero__title{position:absolute;top:102px;width:100%;font-size:60px;font-weight:800;color:#fff;line-height:1;letter-spacing:.5px}

.tag{position:absolute;top:194px;height:36px;background:var(--gold);border-radius:6px;display:flex;align-items:center;justify-content:center;gap:8px;font-weight:700;font-size:18px;color:var(--navy);white-space:nowrap}
.tick{width:14px;height:14px;border-radius:50%;background:var(--navy);display:inline-block;position:relative;flex:none}
.tick::after{content:"";position:absolute;left:4px;top:2.5px;width:4px;height:7px;border:solid var(--gold);border-width:0 2px 2px 0;transform:rotate(45deg)}

.card{position:absolute;border:3px solid var(--gold);border-radius:30px;padding:0 18px}
.card--open-bottom{border-bottom-color:transparent;border-radius:30px 30px 0 0}
.card--open-top{border-top-color:transparent}
.card__icon{position:absolute;top:-22px;left:18px;width:48px;height:44px;background:var(--paper);padding:0 4px}
.card__title{font-size:27px;font-weight:700;line-height:1;color:var(--ink)}
.card__sub{font-size:13px;font-weight:700;text-transform:uppercase;line-height:1.3}

.list{list-style:none}
.list li{font-size:15px;line-height:1.23;padding-left:17px;position:relative;white-space:nowrap}
.list li::before{content:"";position:absolute;left:0;top:6px;width:9px;height:9px;border-radius:50%;background:var(--gold)}
.list--two{display:grid;grid-template-columns:1fr 1fr;column-gap:6px}
.columns{display:flex;gap:8px}
.columns .list{flex:1}
.list--small li{font-size:12px;line-height:1.35;white-space:normal}
.list--small li::before{top:5px;width:8px;height:8px}

.chips{display:flex;gap:7px}
.chip{background:var(--gold);border-radius:6px;font-weight:700;font-size:14px;height:28px;padding:0 10px;display:flex;align-items:center;justify-content:center;color:var(--navy);white-space:nowrap}

.ribbon{display:flex;align-items:center;position:relative;height:46px}
.ribbon__seal{width:50px;height:50px;border-radius:50%;background:var(--gold-soft);color:var(--red);font-weight:800;font-size:23px;display:flex;align-items:center;justify-content:center;z-index:2;border:3px solid var(--seal-ring);flex:none}
.ribbon__bar{background:var(--red);color:#fff;font-weight:700;font-size:17px;height:36px;display:flex;align-items:center;padding:0 22px 0 20px;margin-left:-10px;clip-path:polygon(0 0,100% 0,93% 100%,0 100%);white-space:nowrap}

.note{font-size:15px;line-height:1.25}
.plain{font-size:14px;line-height:1.3}

.photo{position:absolute;left:345px;top:565px;width:260px;height:486px;background:linear-gradient(180deg,#f2f2f2 0%,#e6e6e6 55%,#8a8d92 100%);border-radius:120px 120px 0 0}
.band{position:absolute;left:0;top:1050px;width:940px;height:150px;background:var(--band)}
</style>
</head>
<body>
<header class="hero">
  <div class="hero__kicker">SKILL UP, $ALARY UP</div>
  <h1 class="hero__title">UPCOMING KTA COURSES</h1>
</header>
<div class="tag" style="left:66px;width:202px"><span class="tick"></span>MEN &amp; WOMEN</div>
<div class="tag" style="left:281px;width:276px"><span class="tick"></span>IN-PERSON &amp; REMOTE</div>
<div class="tag" style="left:572px;width:296px"><span class="tick"></span>PARTIAL SCHOLORASHIPS</div>

<section class="card" style="left:66px;top:274px;width:266px;height:378px">
  <svg class="card__icon" viewBox="0 0 48 44"><rect x="4" y="12" width="34" height="24" rx="3" fill="none" stroke="#14203c" stroke-width="3"/><rect x="15" y="6" width="12" height="7" rx="2" fill="none" stroke="#14203c" stroke-width="3"/><circle cx="38" cy="32" r="8" fill="#fff" stroke="#14203c" stroke-width="2.5"/><circle cx="38" cy="30" r="2.5" fill="#14203c"/></svg>
  <h2 class="card__title" style="margin-top:23px">Harbor Lantern Course</h2>
  <div class="card__sub" style="margin-top:10px">Business skills &amp;<br>knowledge to:</div>
  <ul class="list" style="margin-top:6px"><li>Impress your interviewer</li><li>Maximize Income</li><li>Start / Run Your Business</li></ul>
  <div class="chips" style="margin-top:10px"><span class="chip">4-5 MONTHS</span><span class="chip">NOV 2025</span></div>
  <div class="card__sub" style="margin-top:12px">Partial listing</div>
  <div class="columns" style="margin-top:3px">
    <ul class="list list--small"><li>Computers</li><li>Marketing</li><li>Sales</li><li>Finance</li><li>Healthcare</li><li>Communication</li></ul>
    <ul class="list list--small"><li>LedgerBooks</li><li>Investments</li><li>Real Estate</li><li>Accounting</li><li>Business Strategy</li></ul>
  </div>
</section>

<section class="card card--open-bottom" style="left:340px;top:265px;width:266px;height:400px">
  <svg class="card__icon" viewBox="0 0 48 44" style="left:22px;width:40px"><rect x="6" y="2" width="18" height="38" rx="2" fill="#14203c"/><rect x="20" y="18" width="16" height="22" rx="2" fill="#14203c" stroke="#fff" stroke-width="2"/><rect x="24" y="22" width="8" height="4" fill="#fff"/></svg>
  <h2 class="card__title" style="margin-top:32px">Bookkeeping LedgerBooks</h2>
  <div class="card__sub" style="margin-top:14px">Train for a quality job<br>manage your own books</div>
  <div class="card__sub" style="margin-top:14px">Job opportunities</div>
  <ul class="list" style="margin-top:4px"><li>Finance Management</li><li>Customer &amp; Vendor Mgmt.</li><li>Advanced Tools</li></ul>
  <div class="chips" style="margin-top:12px"><span class="chip" style="min-width:108px">5 WEEKS</span><span class="chip">NOV 2025</span></div>
</section>

<section class="card" style="left:613px;top:274px;width:266px;height:378px">
  <svg class="card__icon" viewBox="0 0 48 44"><rect x="3" y="6" width="34" height="24" rx="2" fill="none" stroke="#14203c" stroke-width="3"/><rect x="15" y="30" width="10" height="6" fill="#14203c"/><rect x="10" y="36" width="20" height="3" fill="#14203c"/><circle cx="38" cy="8" r="6" fill="none" stroke="#14203c" stroke-width="3"/></svg>
  <h2 class="card__title" style="margin-top:23px">IT Desktop &amp; Networking Support</h2>
  <div class="ribbon" style="margin-top:14px"><span class="ribbon__seal">#2</span><span class="ribbon__bar" style="width:150px">BEST JOB</span></div>
  <div class="card__sub" style="margin-top:18px">National Career<br>Review 2025</div>
  <div class="card__sub" style="margin-top:12px">Masters IT:</div>
  <ul class="list list--two" style="margin-top:2px"><li>Desktop OS</li><li>Servers</li><li>Networks</li><li>Cloud</li></ul>
  <div class="chips" style="margin-top:14px"><span class="chip" style="min-width:110px">7 MONTHS</span><span class="chip">DEC 2025</span></div>
</section>

<div class="photo" role="img" aria-label="Photo of a smiling young professional in a white collared shirt and grey trousers"></div>

<section class="card card--open-top" style="left:66px;top:687px;width:272px;height:345px">
  <svg class="card__icon" viewBox="0 0 48 44"><rect x="3" y="4" width="32" height="22" rx="2" fill="#14203c"/><text x="8" y="20" font-size="11" fill="#fff" font-family="Poppins,sans-serif">&lt;/&gt;</text><rect x="12" y="28" width="14" height="3" fill="#14203c"/><circle cx="38" cy="30" r="6" fill="none" stroke="#14203c" stroke-width="3"/></svg>
  <h2 class="card__title" style="margin-top:20px">Software,<br>Web &amp; Apps</h2>
  <div class="ribbon" style="margin-top:10px"><span class="ribbon__seal">#2</span><span class="ribbon__bar" style="width:210px">BEST TECH JOB</span></div>
  <div class="card__sub" style="margin-top:10px">National Career Review 2025</div>
  <div class="card__sub" style="margin-top:7px">Job opportunities</div>
  <ul class="list" style="margin-top:2px"><li>Computer Programmer</li><li>Software Developer/Mobile</li><li>Engineer Developer (Apps)</li></ul>
  <div class="card__sub" style="margin-top:8px">Optional:</div>
  <div class="plain">BACHELORS IN PROG. &amp; TECH.</div>
  <div class="chips" style="margin-top:6px"><span class="chip">NOV 2025</span></div>
</section>

<section class="card card--open-top" style="left:608px;top:687px;width:271px;height:347px">
  <svg class="card__icon" viewBox="0 0 48 44" style="top:-20px"><rect x="8" y="4" width="28" height="36" rx="2" fill="none" stroke="#14203c" stroke-width="4"/></svg>
  <h2 class="card__title" style="margin-top:30px">Office<br>Suite<br>Computers</h2>
  <div class="card__sub" style="margin-top:16px">He new job prerequisite</div>
  <ul class="list list--two" style="margin-top:6px"><li>Sheets</li><li>Mail</li><li>Slides</li><li>Docs</li></ul>
  <p class="note" style="margin-top:14px">Computer lab available<br>to practice</p>
  <div class="chips" style="margin-top:10px"><span class="chip" style="min-width:108px">5 WEEKS</span><span class="chip">DEC 2025</span></div>
</section>

<div class="band"></div>
</body>
</html>
```